Medical Aesthetics business cards

Looking for a business card for my new medical aesthetics business. I am a nurse practitioner and will be administering quilen , fillers as well as providing other services

```html
<!DOCTYPE html>
<html lang="en">
<head>
<meta charset="utf-8">
<title>Clara Westmore, APRN-C — Business Card</title>
<link rel="stylesheet" href="https://fonts.googleapis.com/css2?family=Allura&family=Open+Sans:wght@400;600&display=swap">
<style>
  :root {
    --backdrop: #8bb9fb;
    --card: #ffffff;
    --brand-blue: #1f78c1;
    --ornament-light: #cfe2f5;
    --ornament-mid: #7fb2e0;
  }
  html, body {
    margin: 0;
    width: 1200px;
    height: 1200px;
    overflow: hidden;
    background: var(--backdrop);
  }
  .business-card {
    position: absolute;
    left: 100px;
    top: 314px;
    width: 1000px;
    height: 572px;
    background: var(--card);
    border-radius: 28px;
    overflow: hidden;
    color: var(--brand-blue);
    font-family: "Open Sans", Arial, sans-serif;
  }
  .card-frame {
    position: absolute;
    inset: 24px;
    border: 2px solid var(--brand-blue);
  }
  .floral-ornament {
    position: absolute;
    left: -320px;
    top: 40px;
    width: 680px;
    height: 680px;
    border-radius: 50%;
    background: radial-gradient(circle at 45% 40%, var(--ornament-mid), var(--ornament-light) 70%);
  }
  .name-block {
    position: absolute;
    left: 390px;
    right: 58px;
    top: 80px;
    display: flex;
    justify-content: space-between;
    align-items: flex-end;
    white-space: nowrap;
  }
  .practitioner-name {
    margin: 0;
    font-family: "Allura", cursive;
    font-weight: 400;
    font-size: 66px;
    line-height: 1.1;
  }
  .credentials {
    text-align: right;
    padding-bottom: 2px;
  }
  .credentials .title {
    display: block;
    font-size: 38px;
    line-height: 1;
    letter-spacing: 1px;
  }
  .credentials .role {
    display: block;
    font-size: 16px;
    font-weight: 600;
    margin-top: 4px;
  }
  .name-rule {
    position: absolute;
    left: 400px;
    right: 58px;
    top: 200px;
    height: 2px;
    background: var(--brand-blue);
  }
  .contact-list {
    position: absolute;
    left: 480px;
    top: 236px;
    margin: 0;
    padding: 0;
    list-style: none;
    font-size: 24px;
    font-weight: 600;
    letter-spacing: 0.5px;
    white-space: nowrap;
  }
  .contact-list li {
    display: flex;
    align-items: center;
    gap: 14px;
    height: 52px;
  }
  .contact-list svg {
    width: 20px;
    height: 20px;
    flex: none;
  }
  .services-band {
    position: absolute;
    left: 400px;
    top: 440px;
    width: 520px;
    height: 46px;
    background: var(--brand-blue);
    color: var(--card);
    font-size: 26px;
    font-weight: 600;
    line-height: 46px;
    text-align: center;
    letter-spacing: 1px;
    white-space: nowrap;
  }
</style>
</head>
<body>
  <article class="business-card">
    <div class="floral-ornament" role="img" aria-label="Decorative blue line-art flower ornament"></div>
    <div class="card-frame"></div>

    <header class="name-block">
      <h1 class="practitioner-name">Clara Westmore,</h1>
      <div class="credentials">
        <span class="title">APRN-C</span>
        <span class="role">Nurse Practitioner</span>
      </div>
    </header>
    <div class="name-rule"></div>

    <ul class="contact-list">
      <li>
        <svg viewBox="0 0 24 24" aria-hidden="true"><path fill="currentColor" d="M6.6 10.8a15.2 15.2 0 0 0 6.6 6.6l2.2-2.2a1 1 0 0 1 1-.25 11.4 11.4 0 0 0 3.6.57 1 1 0 0 1 1 1V20a1 1 0 0 1-1 1A17 17 0 0 1 3 4a1 1 0 0 1 1-1h3.5a1 1 0 0 1 1 1c0 1.25.2 2.450.57 3.57a1 1 0 0 1-.25 1z"/></svg>
        555-014-2736
      </li>
      <li>
        <svg viewBox="0 0 24 24" aria-hidden="true"><rect x="2.5" y="5" width="19" height="14" fill="none" stroke="currentColor" stroke-width="2"/><path d="M3 6l9 7 9-7" fill="none" stroke="currentColor" stroke-width="2"/></svg>
        info@clearformaesthetics.com
      </li>
      <li>
        <svg viewBox="0 0 24 24" aria-hidden="true"><g fill="none" stroke="currentColor" stroke-width="2"><circle cx="12" cy="12" r="9.5"/><ellipse cx="12" cy="12" rx="4" ry="9.5"/><path d="M2.5 12h19"/></g></svg>
        www.clearformaesthetics.com
      </li>
    </ul>

    <div class="services-band">OFFERING : quilen, fillers, vellara</div>
  </article>
</body>
</html>
```